Reef Glow

sunglasses, sihoullette of body, maybe wearing a bikini or sunglasses. I am offering spray tanning, body wraps, tanning beds, stand up, body art, airbrush makeup.

Target Market(s)

I would say my target is all ages, But tanning is a seasonal business and more beauty and aging concept. and around prom time I get my most profitable business. so 18 to 21 through march and april. then 25 to 55 through april to june.

Industry/Entity Type

Makeup

Contact Information for Business Card

Phone number: 701-382-5147 Owner: Jan Mortby (Lisowski)

Colors

Designer to choose colors to be used in the design.

Requirements
Nice to have
• Sunglasses, silouttes of body wearing sunglasses or bikini, or picture of spray gun.

```html
<!DOCTYPE html>
<html lang="en">
<head>
<meta charset="utf-8">
<title>Jan Mortby Lisowski – Business Card</title>
<link href="https://fonts.googleapis.com/css2?family=Cinzel:wght@500;600&family=Pinyon+Script&family=Cormorant+Garamond:wght@500;700&display=swap" rel="stylesheet">
<style>
  :root {
    --bg-top: #e8e8e9;
    --bg-bottom: #ffffff;
    --gold-light: #e6b752;
    --gold-dark: #a67a2a;
    --green-light: #7a8a3c;
    --green-dark: #1e4626;
    --ink-dark: #2f2a17;
    --phone-brown: #6e5522;
    --umbrella-tone: #f4f4f0;
    --umbrella-shade: #dcdcd6;
  }
  * { margin: 0; padding: 0; box-sizing: border-box; }
  html, body { width: 1200px; height: 702px; overflow: hidden; }
  .card {
    position: relative;
    width: 1200px;
    height: 702px;
    background: linear-gradient(to bottom, var(--bg-top), var(--bg-bottom) 80%);
    overflow: hidden;
  }
  .umbrella-art {
    position: absolute;
    left: 110px;
    top: 190px;
    width: 960px;
    height: 520px;
    border-radius: 50% 50% 20% 30% / 40% 40% 30% 30%;
    background: radial-gradient(ellipse at 55% 35%, var(--umbrella-tone) 0%, rgba(236,236,230,0.85) 45%, rgba(220,220,214,0.35) 75%, rgba(255,255,255,0) 100%);
    transform: rotate(-6deg);
  }
  .owner-first {
    position: absolute;
    left: 0; right: 0;
    top: 108px;
    text-align: center;
    font-family: "Cinzel", serif;
    font-weight: 600;
    font-size: 64px;
    letter-spacing: 1px;
    background: linear-gradient(to bottom, var(--gold-light), var(--gold-dark));
    -webkit-background-clip: text;
    background-clip: text;
    color: transparent;
  }
  .owner-last {
    position: absolute;
    left: 0; right: 0;
    top: 186px;
    text-align: center;
    font-family: "Pinyon Script", cursive;
    font-size: 128px;
    line-height: 1.2;
    background: linear-gradient(to bottom, var(--green-light), var(--green-dark));
    -webkit-background-clip: text;
    background-clip: text;
    color: transparent;
  }
  .services {
    position: absolute;
    left: 0; right: 0;
    top: 410px;
    text-align: center;
    font-family: "Cormorant Garamond", serif;
    font-weight: 700;
    font-size: 19px;
    letter-spacing: 0.6px;
    text-transform: uppercase;
    color: var(--ink-dark);
  }
  .contact {
    position: absolute;
    left: 396px;
    top: 494px;
    display: flex;
    align-items: center;
    gap: 28px;
  }
  .phone-icon { width: 98px; height: 88px; display: block; }
  .phone-numbers {
    font-family: "Cormorant Garamond", serif;
    font-weight: 500;
    font-size: 36px;
    line-height: 50px;
    letter-spacing: 1px;
  }
  .phone-numbers .primary { color: var(--phone-brown); }
  .phone-numbers .secondary { color: var(--ink-dark); }
</style>
</head>
<body>
  <main class="card">
    <div class="umbrella-art" role="img" aria-label="Faint white beach umbrella with wooden pole"></div>

    <h1 class="owner-first">Jan Mortby</h1>
    <p class="owner-last">Lisowski</p>

    <p class="services">Spray tanning, body wraps, tanning beds, stand up, body art, airbrush make up</p>

    <div class="contact">
      <svg class="phone-icon" viewBox="0 0 98 88" aria-hidden="true">
        <defs>
          <linearGradient id="phone-fill" x1="0" y1="0" x2="0" y2="1">
            <stop offset="0" stop-color="#e2b24e"/>
            <stop offset="0.45" stop-color="#9a8a3a"/>
            <stop offset="1" stop-color="#1e4626"/>
          </linearGradient>
        </defs>
        <path fill="url(#phone-fill)" d="M4 22 C4 6 94 6 94 22 L94 30 L72 30 L70 20 L28 20 L26 30 L4 30 Z"/>
        <path fill="url(#phone-fill)" d="M30 26 L68 26 L72 36 L88 58 L88 84 L10 84 L10 58 L26 36 Z"/>
        <circle cx="49" cy="58" r="13" fill="#ffffff"/>
        <circle cx="49" cy="58" r="6" fill="url(#phone-fill)"/>
      </svg>
      <div class="phone-numbers">
        <p class="primary">701- 382 5147</p>
        <p class="secondary">701-264&nbsp; 3098</p>
      </div>
    </div>
  </main>
</body>
</html>
```